High-Converting Facebook Ads for Portals Drapes & Panels (6 Products)

We are looking for a graphic designer to create high-quality Facebook & Instagram ads for our business: Portals Drapes and Panels (Melbourne, Australia).

We require 6 separate ad designs, each for a different product:

Zipscreen Blinds

Outdoor Awnings

Plantation Shutters

Roller Shutters

Security Doors

Roller Blinds & Sheer Curtains

Ad Specifications:

Sizes:

1440 x 1800 px (4:5 ratio)

1080 x 1080 px (1:1 ratio)

1080 x 1920 px (9:16 ratio for Stories/Reels)

Format: PNG (high resolution, not blurry)

Designed specifically for Meta (Facebook/Instagram ads)

Mobile-friendly layout (clear, easy to read)

Style:

Bold, sales-driven, retail-style ads (NOT minimal)

Eye-catching and designed to generate leads

Clean, professional layout

Similar to promotional home improvement ads

Brand Colours:

Red: #E31E24

Blue: #0072BC

White backgrounds

Each ad must include:

“SALE NOW ON” banner at top

Our showroom address:
512 Upper Wattlebank Street, Fennick Vale (must be fully visible, not cut off)

Phone number: 9482 1576

Our logo (provided)

Badge: “Celebrating 13 YEARS in Business” (must be clean and readable)

Call to Action:

For 5 ads: “Book a FREE quote TODAY!”

For Security Doors ad: “ORDER NOW”

Offers / Pricing:

Most products: “UP TO 40% OFF”

Plantation Shutters: “FROM $299/sqm”

Security Doors: “FROM $750”

Content for each ad (examples):

Zipscreen Blinds:

Made to Measure

Fully Installed

Wind, Sun & Insect Protection

Outdoor Awnings:

Reduce Heat & Glare

Energy Saving

Custom Made

Plantation Shutters:

Modern & Elegant

Light & Privacy Control

Durable & Easy Care

Roller Shutters:

Security Protection

Block Heat & Noise

Total Light Control

Security Doors:

3 Point Locking

Premium Mesh

Custom Made

Blinds & Sheers:

Huge Range of Fabrics

Modern Soft Finish

Perfect for Any Room

Important Notes:

All text must be sharp and easy to read (no blur)

Layout must be balanced and not overcrowded

Ensure no text is cut off (especially address and headings)

Badge text must be straight and professional (no distortion)

Use high-quality, relevant images (we will provide references)

Goal:
Create ads that look professional, trustworthy, and generate enquiries/bookings for in-home quotes.

We are open to creative ideas but want a strong, bold retail-style ad that converts.
I have uploaed chatgpt mocks

Target Market(s)

Homeowners in Melbourne, Australia (typically aged 30–65) looking to improve their homes with blinds, shutters, awnings and security doors. Mid to high income households focused on quality, security, and modern home upgrades.

Industry/Entity Type

Home Improvement / Construction / Retail

Font styles to use
Sans Serif

Requirements
Must have
• Clear, bold and easy-to-read text (must be readable on mobile) High-quality, non-blurry design Strong “SALE” style layout (retail promotional look) Proper spacing (no overcrowded designs) All key info visible (address must NOT be cut off) Correct pricing and offers included Clean “13 YEARS” badge (no distortion or curved text) Consistent branding across all 6 ads
Nice to have
• Modern, slightly premium feel while still being bold Good use of contrast (red/blue/white) Subtle shadows or layering to improve depth Clean use of icons or bullet points Strong hierarchy (headline → benefits → offer → CTA) Variations in layout for testing different ad styles
Should not have
• Minimal or plain designs (we want bold, sales-driven ads) Hard-to-read fonts or script fonts Low-quality or blurry images Overcrowded layouts with too much text Important text cut off (especially address or headings) Overuse of effects or “cheap” looking graphics Yellow-heavy colour schemes (must follow brand colours)

```html
<!DOCTYPE html>
<html lang="en">
<head>
<meta charset="utf-8">
<title>Portals Drapes &amp; Panels – Sale Ads</title>
<link rel="stylesheet" href="https://fonts.googleapis.com/css2?family=Anton&family=Oswald:wght@700&family=Poppins:wght@700;800&display=swap">
<style>
:root{
  --page:#a7a7a7;
  --blue:#1d5b96;
  --blue-deep:#123f6e;
  --red:#d4151d;
  --red-deep:#b3121a;
  --ink:#161616;
  --white:#ffffff;
  --gold-hi:#ffe07a;
  --gold:#f2b01e;
  --gold-lo:#c98a0c;
  --badge-blue:#1565c0;
}
*{box-sizing:border-box;margin:0;padding:0}
html,body{width:1200px;height:5352px;overflow:hidden}
body{background:var(--page);position:relative;font-family:"Poppins",sans-serif}

.ad{position:absolute;left:95px;width:1007px;height:1007px;background:var(--blue);overflow:hidden}
.ad-zipscreen{top:93px}
.ad-shutters{top:1133px}
.ad-awnings{top:2174px}
.ad-sheers{top:3214px}
.ad-doors{top:4252px}

.block{position:absolute}
.white{background:var(--white)}
.photo{position:absolute}

/* brand lockup */
.brand{position:absolute;background:var(--white);display:flex;flex-direction:column;align-items:center;justify-content:center;gap:12px}
.brand-mark{width:44px;height:44px;background:var(--red)}
.brand-name{font-family:"Poppins",sans-serif;font-weight:700;color:var(--blue);font-size:36px;line-height:1.1;text-align:center}

/* sale banner */
.sale-banner{position:absolute;z-index:1;transform:rotate(-4deg);transform-origin:left center}
.sale-edge,.sale-face{position:absolute;inset:0}
.sale-edge{background:var(--red);clip-path:polygon(0 10%,100% 0,100% 80%,0 92%);transform:translate(10px,-8px)}
.sale-face{background:var(--ink);clip-path:polygon(0 14%,100% 4%,97% 86%,0 100%)}
.sale-text{position:absolute;inset:0;display:flex;align-items:center;justify-content:center;font-family:"Anton",sans-serif;color:var(--white);letter-spacing:-1px;white-space:nowrap}

.offer-tag{position:absolute;z-index:3;background:linear-gradient(180deg,var(--gold-hi),var(--gold) 60%,var(--gold-lo));clip-path:polygon(0 0,88% 0,100% 100%,0 100%);font-family:"Anton",sans-serif;color:var(--ink);display:flex;align-items:center;padding-left:18px;white-space:nowrap}
.buy-tag{position:absolute;z-index:3;background:var(--red);clip-path:polygon(6% 0,100% 0,100% 100%,0 100%);font-family:"Anton",sans-serif;color:var(--white);display:flex;align-items:center;justify-content:center;transform:rotate(-4deg);white-space:nowrap}

/* features */
.features{position:absolute;list-style:none;color:var(--white);font-family:"Oswald",sans-serif;font-weight:700}
.features li{display:flex;align-items:flex-start;gap:22px}
.features svg{flex:none;stroke:var(--white);fill:none;stroke-width:2.4;stroke-linecap:round;stroke-linejoin:round}
.features.stacked{font-size:56px;line-height:62px}
.features.stacked li{margin-bottom:24px}
.features.stacked svg{width:58px;height:58px;margin-top:6px}
.features.inline{font-size:54px;line-height:60px}
.features.inline li{align-items:center;margin-bottom:34px}
.features.inline svg{width:44px;height:44px}

/* call to action */
.cta{position:absolute;background:var(--white);color:var(--ink);font-weight:800;font-size:42px;line-height:46px;display:flex;flex-direction:column;justify-content:center;padding-left:32px}

/* footer */
.footer{position:absolute;left:0;right:0;top:945px;height:62px;background:var(--red-deep);color:var(--white);font-weight:700;font-size:27px;display:flex;align-items:center;justify-content:space-between;padding:0 30px}
.phone{display:flex;align-items:center;gap:14px;font-size:32px}
.phone svg{width:36px;height:36px;fill:none;stroke:var(--white);stroke-width:2.4;stroke-linecap:round;stroke-linejoin:round}

/* anniversary badge */
.badge{position:absolute;z-index:2;width:var(--d);height:calc(var(--d) * 1.15)}
.badge svg{position:absolute;inset:0;width:100%;height:100%}
.badge-text{position:absolute;left:0;top:0;width:var(--d);height:var(--d);display:flex;flex-direction:column;align-items:center;justify-content:center;color:var(--white);text-align:center}
.badge-small{font-family:"Oswald",sans-serif;font-weight:700;font-size:calc(var(--d) * 0.095);line-height:1.1}
.badge-big{font-family:"Anton",sans-serif;font-size:calc(var(--d) * 0.165);line-height:1.15}
.badge-tiny{font-family:"Oswald",sans-serif;font-weight:700;font-size:calc(var(--d) * 0.07)}

/* ---- zipscreen ---- */
.ad-zipscreen .photo-main{left:461px;top:249px;width:546px;height:696px;background:linear-gradient(160deg,#d9dde0 0%,#8f8a86 35%,#2e2f31 60%,#9c6a4f 80%,#b7b3ac 100%)}
.ad-zipscreen .brand{left:623px;top:83px;width:384px;height:166px}
.ad-zipscreen .sale-banner{left:0;top:93px;width:623px;height:197px}
.ad-zipscreen .sale-text{font-size:104px}
.ad-zipscreen .offer-tag{left:40px;top:26px;width:330px;height:60px;font-size:40px}
.ad-zipscreen .buy-tag{left:365px;top:212px;width:235px;height:72px;font-size:44px}
.ad-zipscreen .features{left:40px;top:322px;width:420px}
.ad-zipscreen .cta{left:0;top:830px;width:461px;height:115px}
.ad-zipscreen .badge{--d:250px;left:689px;top:591px}

/* ---- roller shutters ---- */
.ad-shutters .photo-main{left:0;top:114px;width:623px;height:831px;background:linear-gradient(110deg,#3d5670 0%,#8da2b6 30%,#e9e3dc 55%,#b4542c 70%,#cbc6d8 90%)}
.ad-shutters .brand{left:623px;top:0;width:384px;height:228px}
.ad-shutters .sale-banner{left:0;top:83px;width:623px;height:208px}
.ad-shutters .sale-text{font-size:104px}
.ad-shutters .offer-tag{left:20px;top:30px;width:290px;height:55px;font-size:36px}
.ad-shutters .buy-tag{left:349px;top:218px;width:239px;height:72px;font-size:44px}
.ad-shutters .features{left:648px;top:318px;width:350px}
.ad-shutters .cta{left:623px;top:816px;width:384px;height:129px;padding-left:24px}
.ad-shutters .badge{--d:260px;left:76px;top:584px}

/* ---- awnings ---- */
.ad-awnings .brand{left:619px;top:0;width:388px;height:197px}
.ad-awnings .photo-top{left:619px;top:197px;width:388px;height:391px;background:linear-gradient(120deg,#f2f0ee 0%,#d33a3f 30%,#f6f2ef 50%,#cf3238 70%,#e8e4e0 100%)}
.ad-awnings .photo-bottom{left:0;top:588px;width:619px;height:357px;background:linear-gradient(170deg,#c9d7e2 0%,#d05a52 30%,#efe6dc 45%,#8b7a64 70%,#4d5a3a 100%)}
.ad-awnings .panel-white{left:619px;top:588px;width:388px;height:357px}
.ad-awnings .sale-banner{left:0;top:73px;width:500px;height:166px}
.ad-awnings .sale-text{font-size:86px}
.ad-awnings .offer-tag{left:40px;top:26px;width:230px;height:46px;font-size:29px}
.ad-awnings .buy-tag{left:290px;top:176px;width:198px;height:60px;font-size:36px}
.ad-awnings .features{left:30px;top:292px;width:580px}
.ad-awnings .cta{left:619px;top:790px;width:388px;height:140px;padding-left:32px;background:transparent}
.ad-awnings .badge{--d:230px;left:686px;top:524px}

/* ---- sheers ---- */
.ad-sheers .photo-main{left:0;top:0;width:592px;height:945px;background:linear-gradient(90deg,#8a8a86 0%,#e7e7e3 25%,#f7f7f5 50%,#5b5450 60%,#ecebe8 75%,#9a9893 100%)}
.ad-sheers .brand{left:592px;top:0;width:415px;height:218px}
.ad-sheers .sale-banner{left:31px;top:58px;width:498px;height:176px}
.ad-sheers .sale-text{font-size:88px}
.ad-sheers .offer-tag{left:73px;top:10px;width:240px;height:46px;font-size:31px}
.ad-sheers .buy-tag{left:332px;top:176px;width:187px;height:56px;font-size:36px}
.ad-sheers .features{left:616px;top:300px;width:385px}
.ad-sheers .cta{left:592px;top:764px;width:415px;height:181px;padding-left:40px}
.ad-sheers .badge{--d:260px;left:370px;top:622px}

/* ---- security doors ---- */
.ad-doors .brand{left:0;top:0;width:409px;height:214px}
.ad-doors .photo-main{left:592px;top:0;width:415px;height:945px;background:linear-gradient(180deg,#6b4a32 0%,#d9d6d2 8%,#4a3a33 20%,#d0cdc8 30%,#43342e 50%,#cfccc7 65%,#3f312b 85%,#5a4634 100%)}
.ad-doors .offer-tag{left:31px;top:234px;width:290px;height:52px;font-size:36px}
.ad-doors .sale-banner{left:0;top:291px;width:560px;height:166px}
.ad-doors .sale-text{font-size:96px}
.ad-doors .buy-tag{left:332px;top:413px;width:203px;height:58px;font-size:38px}
.ad-doors .features{left:36px;top:512px;width:560px}
.ad-doors .features.inline li{margin-bottom:31px}
.ad-doors .cta-order{position:absolute;left:0;top:795px;width:592px;height:150px;background:var(--white)}
.ad-doors .lock-photo{left:28px;top:10px;width:118px;height:130px;background:linear-gradient(90deg,#1a1a1a,#4a4a4a 50%,#1a1a1a)}
.ad-doors .door-thumb{left:392px;top:12px;width:84px;height:126px;background:linear-gradient(180deg,#2a2a2a,#5b4a3c)}
.ad-doors .order-text{position:absolute;left:150px;top:0;width:240px;height:150px;display:flex;flex-direction:column;align-items:center;justify-content:center;font-weight:800;font-size:54px;line-height:56px;color:var(--ink)}
.ad-doors .badge{--d:210px;left:493px;top:657px}
</style>
</head>
<body>

<!-- Zipscreen blinds -->
<section class="ad ad-zipscreen">
  <div class="photo photo-main" role="img" aria-label="Hand holding a remote in front of a lowered zipscreen blind on a brick porch"></div>
  <div class="brand"><span class="brand-mark"></span><span class="brand-name">Portals Drapes<br>&amp; Panels</span></div>
  <div class="sale-banner"><span class="sale-edge"></span><span class="sale-face"></span><span class="sale-text">SALE NOW ON</span></div>
  <div class="offer-tag">UP TO 40% OFF</div>
  <div class="buy-tag">BUY NOW</div>
  <ul class="features stacked">
    <li><svg viewBox="0 0 32 32"><circle cx="13" cy="14" r="9"/><path d="M13 23h16v5H13M13 14h0.01"/></svg><span>Made<br>to Measure</span></li>
    <li><svg viewBox="0 0 32 32"><path d="M5 27 19 13M22 4a6 6 0 0 0-5 8l10 10M5 5l22 22"/></svg><span>Fully<br>Installed</span></li>
    <li><svg viewBox="0 0 32 32"><path d="M16 3 5 7v8c0 7 5 12 11 14 6-2 11-7 11-14V7z"/><path d="m11 16 4 4 7-8"/></svg><span>Wind, Sun<br>&amp; Insect<br>Protection</span></li>
  </ul>
  <div class="cta"><span>Book a FREE</span><span>quote TODAY!</span></div>
  <div class="badge">
    <svg viewBox="0 0 100 115"><defs><radialGradient id="g1" cx="40%" cy="35%"><stop offset="0" stop-color="#ffe27a"/><stop offset=".6" stop-color="#f2b01e"/><stop offset="1" stop-color="#c98a0c"/></radialGradient></defs><polygon points="28,70 46,82 36,112 29,101 18,108" fill="#1d5b96"/><polygon points="72,70 54,82 64,112 71,101 82,108" fill="#1d5b96"/><circle cx="50" cy="50" r="48" fill="url(#g1)"/><circle cx="50" cy="50" r="36" fill="#1565c0" stroke="#fff3c4" stroke-width="2"/></svg>
    <div class="badge-text"><span class="badge-small">Celebrating</span><span class="badge-big">13 YEARS</span><span class="badge-tiny">in Business</span></div>
  </div>
  <footer class="footer"><span>512 Upper Wattlebank Street, Fennick Vale</span><span class="phone"><svg viewBox="0 0 24 24"><path d="M5 3h4l2 5-2.5 1.5a11 11 0 0 0 6 6L16 13l5 2v4a2 2 0 0 1-2 2A16 16 0 0 1 3 5a2 2 0 0 1 2-2z"/></svg>9482 1576</span></footer>
</section>

<!-- Roller shutters -->
<section class="ad ad-shutters">
  <div class="photo photo-main" role="img" aria-label="Woman opening roller shutter slats beside a window"></div>
  <div class="brand"><span class="brand-mark"></span><span class="brand-name">Portals Drapes<br>&amp; Panels</span></div>
  <div class="sale-banner"><span class="sale-edge"></span><span class="sale-face"></span><span class="sale-text">SALE NOW ON</span></div>
  <div class="offer-tag">UP TO 40% OFF</div>
  <div class="buy-tag">BUY NOW</div>
  <ul class="features stacked">
    <li><svg viewBox="0 0 32 32"><path d="M16 3 5 7v8c0 7 5 12 11 14 6-2 11-7 11-14V7z"/><path d="m11 16 4 4 7-8"/></svg><span>Security<br>Protection</span></li>
    <li><svg viewBox="0 0 32 32"><path d="M3 16 14 6l11 10M6 14v13h16V14M12 20h4v4h-4z"/><path d="M27 4l-2 6h4l-2 6"/></svg><span>Block Heat<br>&amp; Noise</span></li>
    <li><svg viewBox="0 0 32 32"><rect x="4" y="8" width="24" height="16"/><path d="M16 3v3M8 28h16M10 16a6 6 0 0 1 12 0"/></svg><span>Total Light<br>Control</span></li>
  </ul>
  <div class="cta"><span>Book a FREE</span><span>quote TODAY!</span></div>
  <div class="badge">
    <svg viewBox="0 0 100 115"><defs><radialGradient id="g2" cx="40%" cy="35%"><stop offset="0" stop-color="#ffe27a"/><stop offset=".6" stop-color="#f2b01e"/><stop offset="1" stop-color="#c98a0c"/></radialGradient></defs><polygon points="28,70 46,82 36,112 29,101 18,108" fill="#1d5b96"/><polygon points="72,70 54,82 64,112 71,101 82,108" fill="#1d5b96"/><circle cx="50" cy="50" r="48" fill="url(#g2)"/><circle cx="50" cy="50" r="36" fill="#1565c0" stroke="#fff3c4" stroke-width="2"/></svg>
    <div class="badge-text"><span class="badge-small">Celebrating</span><span class="badge-big">13 YEARS</span><span class="badge-tiny">in Business</span></div>
  </div>
  <footer class="footer"><span>512 Upper Wattlebank Street, Fennick Vale</span><span class="phone"><svg viewBox="0 0 24 24"><path d="M5 3h4l2 5-2.5 1.5a11 11 0 0 0 6 6L16 13l5 2v4a2 2 0 0 1-2 2A16 16 0 0 1 3 5a2 2 0 0 1 2-2z"/></svg>9482 1576</span></footer>
</section>

<!-- Outdoor awnings -->
<section class="ad ad-awnings">
  <div class="brand"><span class="brand-mark"></span><span class="brand-name">Portals Drapes<br>&amp; Panels</span></div>
  <div class="photo photo-top" role="img" aria-label="Red and white striped awnings on a building facade"></div>
  <div class="photo photo-bottom" role="img" aria-label="Striped folding-arm awning over a stone patio"></div>
  <div class="block white panel-white"></div>
  <div class="sale-banner"><span class="sale-edge"></span><span class="sale-face"></span><span class="sale-text">SALE NOW ON</span></div>
  <div class="offer-tag">UP TO 40% OFF</div>
  <div class="buy-tag">BUY NOW</div>
  <ul class="features inline">
    <li><svg viewBox="0 0 32 32"><circle cx="18" cy="16" r="6"/><path d="M18 4v3M18 25v3M28 16h-3M7 10v14a3 3 0 1 0 4 0V10a2 2 0 0 0-4 0z"/></svg><span>Reduce Heat &amp; Glare</span></li>
    <li><svg viewBox="0 0 32 32"><rect x="9" y="4" width="14" height="24" rx="2"/><path d="M13 4V2h6v2M13 20h6M13 15h6"/></svg><span>Energy Saving</span></li>
    <li><svg viewBox="0 0 32 32"><path d="M6 4v24M16 4v24M26 4v24M3 10h6M13 20h6M23 13h6"/></svg><span>Custom Made</span></li>
  </ul>
  <div class="badge">
    <svg viewBox="0 0 100 115"><defs><radialGradient id="g3" cx="40%" cy="35%"><stop offset="0" stop-color="#ffe27a"/><stop offset=".6" stop-color="#f2b01e"/><stop offset="1" stop-color="#c98a0c"/></radialGradient></defs><polygon points="28,70 46,82 36,112 29,101 18,108" fill="#1d5b96"/><polygon points="72,70 54,82 64,112 71,101 82,108" fill="#1d5b96"/><circle cx="50" cy="50" r="48" fill="url(#g3)"/><circle cx="50" cy="50" r="36" fill="#1565c0" stroke="#fff3c4" stroke-width="2"/></svg>
    <div class="badge-text"><span class="badge-small">Celebrating</span><span class="badge-big">13 YEARS</span><span class="badge-tiny">in Business</span></div>
  </div>
  <div class="cta"><span>Book a FREE</span><span>quote TODAY!</span></div>
  <footer class="footer"><span>512 Upper Wattlebank Street, Fennick Vale</span><span class="phone"><svg viewBox="0 0 24 24"><path d="M5 3h4l2 5-2.5 1.5a11 11 0 0 0 6 6L16 13l5 2v4a2 2 0 0 1-2 2A16 16 0 0 1 3 5a2 2 0 0 1 2-2z"/></svg>9482 1576</span></footer>
</section>

<!-- Roller blinds & sheer curtains -->
<section class="ad ad-sheers">
  <div class="photo photo-main" role="img" aria-label="Girl parting sheer curtains in a bright room"></div>
  <div class="brand"><span class="brand-mark"></span><span class="brand-name">Portals Drapes<br>&amp; Panels</span></div>
  <div class="sale-banner"><span class="sale-edge"></span><span class="sale-face"></span><span class="sale-text">SALE NOW ON</span></div>
  <div class="offer-tag">UP TO 40% OFF</div>
  <div class="buy-tag">BUY NOW</div>
  <ul class="features stacked">
    <li><svg viewBox="0 0 32 32"><path d="M16 4 3 11l13 7 13-7zM3 16l13 7 13-7M3 21l13 7 13-7"/></svg><span>Huge Range<br>of Fabrics</span></li>
    <li><svg viewBox="0 0 32 32"><path d="M27 4C14 6 7 14 5 28M27 4c0 12-8 18-18 18M12 16h7"/></svg><span>Modern Soft<br>Finish</span></li>
    <li><svg viewBox="0 0 32 32"><circle cx="16" cy="16" r="11"/><path d="m16 10 2 4 4 .5-3 3 .8 4.5-3.8-2-3.8 2 .8-4.5-3-3 4-.5z"/></svg><span>Perfect for<br>Any Room</span></li>
  </ul>
  <div class="cta"><span>Book a FREE</span><span>quote TODAY!</span></div>
  <div class="badge">
    <svg viewBox="0 0 100 115"><defs><radialGradient id="g4" cx="40%" cy="35%"><stop offset="0" stop-color="#ffe27a"/><stop offset=".6" stop-color="#f2b01e"/><stop offset="1" stop-color="#c98a0c"/></radialGradient></defs><polygon points="28,70 46,82 36,112 29,101 18,108" fill="#1d5b96"/><polygon points="72,70 54,82 64,112 71,101 82,108" fill="#1d5b96"/><circle cx="50" cy="50" r="48" fill="url(#g4)"/><circle cx="50" cy="50" r="36" fill="#1565c0" stroke="#fff3c4" stroke-width="2"/></svg>
    <div class="badge-text"><span class="badge-small">Celebrating</span><span class="badge-big">13 YEARS</span><span class="badge-tiny">in Business</span></div>
  </div>
  <footer class="footer"><span>512 Upper Wattlebank Street, Fennick Vale</span><span class="phone"><svg viewBox="0 0 24 24"><path d="M5 3h4l2 5-2.5 1.5a11 11 0 0 0 6 6L16 13l5 2v4a2 2 0 0 1-2 2A16 16 0 0 1 3 5a2 2 0 0 1 2-2z"/></svg>9482 1576</span></footer>
</section>

<!-- Security doors -->
<section class="ad ad-doors">
  <div class="brand"><span class="brand-mark"></span><span class="brand-name">Portals Drapes<br>&amp; Panels</span></div>
  <div class="photo photo-main" role="img" aria-label="Dark timber-look security door with a tall vertical handle"></div>
  <div class="sale-banner"><span class="sale-edge"></span><span class="sale-face"></span><span class="sale-text">SALE NOW ON</span></div>
  <div class="offer-tag">FROM $750</div>
  <div class="buy-tag">BUY NOW</div>
  <ul class="features inline">
    <li><svg viewBox="0 0 32 32"><path d="M10 4h8v18h8v6H10zM14 10h0.01M14 16h0.01"/></svg><span>3 Point Locking</span></li>
    <li><svg viewBox="0 0 32 32"><rect x="5" y="5" width="22" height="22"/><path d="M12 5v22M20 5v22M5 12h22M5 20h22"/></svg><span>Premium Mesh</span></li>
    <li><svg viewBox="0 0 32 32"><path d="M14 4h12v24H14z"/><circle cx="8" cy="20" r="4"/><path d="M18 16h0.01"/></svg><span>Custom Made</span></li>
  </ul>
  <div class="cta-order">
    <div class="photo lock-photo" role="img" aria-label="Black keypad door lock set"></div>
    <div class="order-text"><span>ORDER</span><span>NOW</span></div>
    <div class="photo door-thumb" role="img" aria-label="Small security door product shot"></div>
  </div>
  <div class="badge">
    <svg viewBox="0 0 100 115"><defs><radialGradient id="g5" cx="40%" cy="35%"><stop offset="0" stop-color="#ffe27a"/><stop offset=".6" stop-color="#f2b01e"/><stop offset="1" stop-color="#c98a0c"/></radialGradient></defs><polygon points="28,70 46,82 36,112 29,101 18,108" fill="#1d5b96"/><polygon points="72,70 54,82 64,112 71,101 82,108" fill="#1d5b96"/><circle cx="50" cy="50" r="48" fill="url(#g5)"/><circle cx="50" cy="50" r="36" fill="#1565c0" stroke="#fff3c4" stroke-width="2"/></svg>
    <div class="badge-text"><span class="badge-small">Celebrating</span><span class="badge-big">13 YEARS</span><span class="badge-tiny">in Business</span></div>
  </div>
  <footer class="footer"><span>512 Upper Wattlebank Street, Fennick Vale</span><span class="phone"><svg viewBox="0 0 24 24"><path d="M5 3h4l2 5-2.5 1.5a11 11 0 0 0 6 6L16 13l5 2v4a2 2 0 0 1-2 2A16 16 0 0 1 3 5a2 2 0 0 1 2-2z"/></svg>9482 1576</span></footer>
</section>

</body>
</html>
```